Cloud Phone Service Brochure

We need a brochure for a Cloud Phone Service offering that we offer in Canada. We're a small company that cares about our client's success and protects their privacy. We would like to see designs that reflect us as a stable, trustworthy company which is also fast moving and leading edge. We see ourselves more like Zelmo than Hask. Sketch Harbor has built our logo and business card, and we look forward to moving ahead here. I've attached our Business Card file so you have our logo as well as my own shot at some thoughts about content written as a trifold. That specific content does not need to be used, nor does it need to be a trifold. Those phone pictures are the actual phones we use.

```html
<!DOCTYPE html>
<html lang="en">
<head>
<meta charset="utf-8">
<title>Bright Current Consulting – Cloud Phone Service Brochure</title>
<link rel="stylesheet" href="https://fonts.googleapis.com/css2?family=Oswald:wght@300;400;600&family=Montserrat:wght@400;600;700&display=swap">
<style>
  :root{
    --blue:#1a8fd6;
    --blue-dark:#116fb0;
    --ink:#3a3a3a;
    --ink-soft:#666;
    --paper:#f4f4f4;
    --paper-edge:#e4e4e4;
    --stage:#d6d6d6;
    --photo-brown:#3b2a22;
    --photo-orange:#f0a33a;
  }
  *{box-sizing:border-box;margin:0;padding:0}
  html,body{width:1200px;height:2190px;overflow:hidden}
  body{background:var(--stage);font-family:"Montserrat",sans-serif;color:var(--ink)}

  .spread{position:absolute;left:20px;width:1160px;height:820px;display:grid;grid-template-columns:386px 388px 386px;
    background:var(--paper);box-shadow:0 6px 24px rgba(0,0,0,.18)}
  .spread--outside{top:190px}
  .spread--inside{top:1170px}
  .panel{position:relative;overflow:hidden;border-right:1px solid var(--paper-edge)}
  .panel:last-child{border-right:none}

  .photo{position:absolute}
  .photo--top-curve{left:0;top:0;width:100%;height:220px;border-bottom:7px solid var(--blue);border-right:7px solid var(--blue);border-bottom-right-radius:140px}
  .photo--bottom-curve{right:0;bottom:0;width:88%;height:250px;border-top:7px solid var(--blue);border-left:7px solid var(--blue);border-top-left-radius:140px}

  .panel-body{position:absolute;left:34px;right:28px}
  .heading{font-family:"Montserrat",sans-serif;font-weight:700;font-size:15px;line-height:1.15;text-transform:uppercase;color:var(--ink);margin:18px 0 8px}
  .heading span{color:var(--blue)}
  .heading:first-child{margin-top:0}
  .list{list-style:none;font-size:11.2px;line-height:1.42}
  .list li{position:relative;padding-left:15px}
  .list li::before{content:"";position:absolute;left:0;top:5px;width:7px;height:7px;background:var(--blue);border-radius:1px}
  .list li.sub{padding-left:28px}
  .list li.sub::before{left:14px;background:none;border:1.5px solid var(--blue);border-radius:50%}
  .list--para li{margin-bottom:5px}

  /* outside: partners panel */
  .partners{display:grid;grid-template-columns:repeat(3,1fr);gap:10px;margin-bottom:8px}
  .badge{height:34px;background:#fff;border:1px solid #ddd;border-radius:4px;box-shadow:0 1px 3px rgba(0,0,0,.1);position:relative}
  .badge::after{content:"";position:absolute;left:30%;right:30%;top:13px;height:8px;border-radius:4px;background:var(--badge,#bbb)}

  /* outside: contact panel */
  .contact{position:absolute;left:0;right:0;top:360px;text-align:center;font-size:13px;line-height:1.45;color:var(--ink)}
  .contact .icon{display:block;margin:14px auto 4px;width:20px;height:20px}
  .brand{display:inline-flex;align-items:center;gap:8px;font-family:"Montserrat",sans-serif;font-weight:600;font-size:15px;letter-spacing:.06em;text-transform:uppercase;color:var(--blue)}
  .brand::before{content:"";width:22px;height:22px;background:var(--blue)}

  /* cover */
  .cover-art{position:absolute;inset:0}
  .cover-copy{position:absolute;left:34px;right:24px;top:540px}
  .cover-copy .brand{font-size:14px}
  .title{font-family:"Oswald",sans-serif;font-weight:600;font-size:52px;line-height:1;text-transform:uppercase;color:var(--ink);margin-top:30px;letter-spacing:-.01em}
  .subtitle{font-family:"Oswald",sans-serif;font-weight:300;font-size:38px;line-height:1.05;text-transform:uppercase;color:var(--blue)}
  .web{font-size:14px;letter-spacing:.04em;color:var(--ink);margin-top:18px}

  .device{position:absolute;border-radius:6px}
</style>
</head>
<body>

<!-- OUTSIDE OF TRIFOLD -->
<section class="spread spread--outside">

  <article class="panel panel--partners">
    <div class="photo photo--top-curve" role="img" aria-label="Photo of a desk video phone showing a video call on its screen"
         style="background:linear-gradient(160deg,#2b2f36 0%,#4a525c 55%,#9aa4ad 100%)"></div>
    <div class="panel-body" style="top:270px">
      <h2 class="heading">Our <span>Partners</span></h2>
      <div class="partners">
        <div class="badge" style="--badge:#d0463b"></div>
        <div class="badge" style="--badge:#4a86e8"></div>
        <div class="badge" style="--badge:#e04b4b"></div>
        <div class="badge" style="--badge:#555"></div>
        <div class="badge" style="--badge:#6aa84f"></div>
        <div class="badge" style="--badge:#3c78d8"></div>
        <div class="badge" style="--badge:#7bb662"></div>
        <div class="badge" style="--badge:#cc3333"></div>
        <div class="badge" style="--badge:#333"></div>
      </div>
      <h2 class="heading">We <span>Are</span></h2>
      <ul class="list">
        <li>~70% Renewable Energy</li>
        <li>100% Renewable for 2020</li>
      </ul>
      <h2 class="heading">We give our time and<br>skills to help</h2>
      <ul class="list">
        <li>Schools</li>
        <li>Community Associations</li>
        <li>Non-profits</li>
        <li>Renewable Energy Initiatives</li>
      </ul>
    </div>
  </article>

  <article class="panel panel--contact">
    <div class="contact">
      <div class="brand">Bright Current Consulting</div>
      <svg class="icon" viewBox="0 0 24 24" aria-hidden="true"><path fill="var(--blue)" d="M6.6 10.8a15 15 0 0 0 6.6 6.6l2.2-2.2a1 1 0 0 1 1-.25 11.4 11.4 0 0 0 3.6.57 1 1 0 0 1 1 1V20a1 1 0 0 1-1 1A17 17 0 0 1 3 4a1 1 0 0 1 1-1h3.5a1 1 0 0 1 1 1c0 1.25.2 2.45.57 3.57a1 1 0 0 1-.25 1z"/></svg>
      <div>(403) 555-0142</div>
      <svg class="icon" viewBox="0 0 24 24" aria-hidden="true"><circle cx="12" cy="12" r="9" fill="none" stroke="var(--blue)" stroke-width="2"/><path d="M3 12h18M12 3c3 3 3 15 0 18M12 3c-3 3-3 15 0 18" fill="none" stroke="var(--blue)" stroke-width="1.6"/></svg>
      <div>www.yourwebsite.com</div>
      <svg class="icon" viewBox="0 0 24 24" aria-hidden="true"><path fill="var(--blue)" d="M12 2a7 7 0 0 0-7 7c0 5.2 7 13 7 13s7-7.8 7-13a7 7 0 0 0-7-7zm0 9.5A2.5 2.5 0 1 1 12 6.5a2.5 2.5 0 0 1 0 5z"/></svg>
      <div>PO Box 31820<br>14-4410 Harrow Ridge Road NW<br>Calgary, Alberta T3P 0K2<br>Canada</div>
    </div>
  </article>

  <article class="panel panel--cover">
    <svg class="cover-art" viewBox="0 0 386 820" preserveAspectRatio="none" aria-hidden="true">
      <defs>
        <linearGradient id="coverTone" x1="0" y1="0" x2="1" y2="1">
          <stop offset="0" stop-color="#5a4034"/>
          <stop offset=".55" stop-color="var(--photo-brown)"/>
          <stop offset="1" stop-color="#1f1712"/>
        </linearGradient>
        <radialGradient id="coverGlow" cx=".55" cy=".42" r=".35">
          <stop offset="0" stop-color="var(--photo-orange)" stop-opacity=".85"/>
          <stop offset="1" stop-color="var(--photo-orange)" stop-opacity="0"/>
        </radialGradient>
      </defs>
      <rect width="386" height="500" fill="url(#coverTone)"/>
      <rect width="386" height="500" fill="url(#coverGlow)"/>
      <polygon points="0,470 150,330 290,470 386,430 386,820 0,820" fill="var(--paper)"/>
      <polyline points="-10,440 150,290 330,470" fill="none" stroke="var(--blue)" stroke-width="26" stroke-linejoin="miter"/>
      <polygon points="316,480 386,430 386,446 330,486" fill="var(--blue)"/>
    </svg>
    <div role="img" aria-label="Photo of open hands beneath glowing cloud and network icons" style="position:absolute;left:0;top:0;width:386px;height:300px"></div>
    <div class="cover-copy">
      <div class="brand">Bright Current Consulting</div>
      <h1 class="title">Get Connected</h1>
      <p class="subtitle">Anywhere Anytime!</p>
      <p class="web">www.yourwebsite.com</p>
    </div>
  </article>
</section>

<!-- INSIDE OF TRIFOLD -->
<section class="spread spread--inside">

  <article class="panel panel--why">
    <div class="photo photo--top-curve" role="img" aria-label="Photo of a bright conference room with a large video call screen"
         style="background:linear-gradient(170deg,#eef2f5 0%,#cfd8df 60%,#aebbc5 100%)"></div>
    <div class="panel-body" style="top:250px">
      <h2 class="heading">Why <span>Cloud<br>Service?</span></h2>
      <ul class="list list--para">
        <li>Cloud Phones mean no setup costs and no hardware to purchase or support.</li>
        <li>Cloud service also offers seamless remote working and multi-office collaboration.</li>
      </ul>
      <h2 class="heading">Why Bright <span>Current?</span></h2>
      <ul class="list list--para">
        <li>Bright Current believes in building long term collaborative relationships.</li>
        <li>We care about your business as if it was our own.</li>
        <li>Your privacy matters to us. We do not sell, rent or share your data.</li>
      </ul>
      <h2 class="heading">Phone<br><span>Service Features:</span></h2>
      <ul class="list">
        <li>All features and functions included</li>
        <li>Conference line included</li>
        <li>Toll Free Number included</li>
        <li>North American LD included</li>
        <li>Monthly billing with no contract</li>
        <li>No hardware or installation costs</li>
        <li>Any high speed internet service</li>
        <li>Keep your existing phone number</li>
        <li>Voicemail to email</li>
        <li>Find Me &amp; Follow Me</li>
        <li>Call Recording</li>
      </ul>
    </div>
    <div class="device" role="img" aria-label="Photo of a conference speakerphone with camera"
         style="right:22px;bottom:26px;width:86px;height:58px;background:radial-gradient(ellipse at 50% 70%,#3a3a3a 0%,#1c1c1c 60%,rgba(0,0,0,0) 72%)"></div>
  </article>

  <article class="panel panel--video">
    <div class="panel-body" style="top:44px">
      <h2 class="heading">Video Conferencing<br><span>Room Configuration</span></h2>
      <ul class="list">
        <li>120 Simultaneous video streams supported</li>
        <li>Most conference sources</li>
        <li class="sub">Video Conf Room System</li>
        <li class="sub">Video Phones</li>
        <li class="sub">Desktop &amp; Laptop Computers</li>
        <li class="sub">Tablet &amp; Mobile Devices</li>
        <li class="sub">SIP PBXes</li>
        <li class="sub">PSTN Phones</li>
        <li>Connect StreamTube &amp; Friendcast Live</li>
        <li>1080p HD at 30 fps</li>
        <li>Multi-location conferencing</li>
        <li>Meeting Controls</li>
        <li>Screen Sharing</li>
        <li>Customizable Registration options</li>
        <li>Email Follow-up options</li>
        <li>10 simultaneous sessions</li>
        <li>Encrypted connections</li>
      </ul>
      <h2 class="heading" style="margin-top:26px">IP Video <span>Telephony</span></h2>
      <ul class="list">
        <li>HD Speakerphone</li>
        <li>HD Video</li>
        <li>7" Touch screen</li>
        <li>Supports Bluetooth Headsets</li>
        <li>Built in camera &amp; privacy shutter</li>
        <li>7-way video conferences on device</li>
        <li>Fully interoperable with our other phone services</li>
        <li>Ideal for remote workers</li>
        <li>Any high-speed internet service</li>
        <li>Video Conference Room solutions available</li>
      </ul>
    </div>
  </article>

  <article class="panel panel--services">
    <div class="device" role="img" aria-label="Photo of a black desk IP phone"
         style="right:22px;top:22px;width:96px;height:78px;background:linear-gradient(160deg,#4a4a4a,#151515)"></div>
    <div class="panel-body" style="top:44px">
      <h2 class="heading">Our <span>Services</span></h2>
      <ul class="list">
        <li>Network Support</li>
        <li>Phone Service</li>
        <li>Disaster Recovery</li>
        <li>Remote Backups</li>
        <li>Email Archiving</li>
        <li>Office Suite &amp; Cloud Apps</li>
        <li>Migration Services</li>
        <li>Spam and Virus Filtering</li>
        <li>Server and Network Monitoring</li>
        <li>Printing, Scanning and Plotting</li>
        <li>Firewalls and Security</li>
        <li>Network Design and Planning</li>
        <li>Network and Electrical Cabling</li>
        <li>Wireless coverage planning</li>
        <li>Security cameras &amp; Access Control</li>
      </ul>
    </div>
    <div class="photo photo--bottom-curve" role="img" aria-label="Photo of a businessman holding a glowing globe made of media screens"
         style="background:radial-gradient(circle at 45% 45%,#7d93a8 0%,#3c4f66 35%,#1b2433 75%)"></div>
  </article>
</section>

</body>
</html>
```